Change an Existing THEME on a Shopify Site

We currently have a Shopify Site that we would like to launch soon. We picked a current theme [Vesta] and have made some basic changes to it but we don't really know what we're doing. We would like a new theme based on this one specifically built for our site. We already brand colours and a logo.

```html
<!DOCTYPE html>
<html lang="en">
<head>
<meta charset="utf-8">
<title>Maple Paws – Home</title>
<link href="https://fonts.googleapis.com/css2?family=Montserrat:wght@600;700&family=Poppins:ital,wght@0,400;0,500;0,600;1,400&display=swap" rel="stylesheet">
<style>
:root{
  --navy:#14245a;
  --navy-dark:#0f1c48;
  --teal:#9fd7d3;
  --teal-btn:#80d4ce;
  --teal-soft:#e8fafa;
  --grey-bg:#f4f4f4;
  --text:#333a4d;
  --white:#fff;
  --accent:#e0662a;
  --star:#f3b51b;
}
*{box-sizing:border-box;margin:0;padding:0}
html,body{width:1200px;height:3947px;overflow:hidden}
body{position:relative;font-family:"Poppins",sans-serif;color:var(--text);background:var(--white)}
.abs{position:absolute}
h1,h2,.heading{font-family:"Montserrat",sans-serif;color:var(--navy);font-weight:700}
.pill{position:absolute;display:flex;align-items:center;justify-content:center;gap:14px;border-radius:40px;font-weight:600;font-family:"Poppins",sans-serif}
.pill--navy{background:var(--navy);color:var(--white)}
.pill .dot{width:20px;height:20px;border-radius:50%;background:var(--teal);display:flex;align-items:center;justify-content:center}
.brand-mark{position:absolute;border-radius:50%;background:var(--teal);display:flex;align-items:center;justify-content:center;text-align:center;color:var(--navy);font-weight:600;line-height:1.1}

/* header */
.nav{position:absolute;top:42px;left:550px;display:flex;gap:34px;font-size:14px;color:var(--navy)}
.nav .active{color:var(--accent);border-bottom:2px solid var(--accent);padding-bottom:6px}
.btn-cart{position:absolute;top:36px;left:919px;width:113px;height:32px;background:var(--teal);border-radius:16px;font-size:12px;color:var(--navy);display:flex;align-items:center;justify-content:center;gap:8px}
.btn-login{position:absolute;top:36px;left:1043px;width:92px;height:32px;background:var(--navy);border-radius:16px;font-size:12px;color:var(--white);display:flex;align-items:center;justify-content:center;gap:8px}

/* hero */
.hero-bg{top:103px;left:0;width:1200px;height:671px;background:var(--grey-bg)}
.hero-title{top:262px;left:62px;font-size:104px;line-height:96px;letter-spacing:1px}
.hero-text{top:480px;left:69px;width:480px;font-size:20px;line-height:32px}
.hero-photo{top:135px;left:598px;width:602px;height:660px}

/* features */
.feature{position:absolute;top:843px;display:flex;align-items:center;gap:22px}
.feature .ring{width:96px;height:96px;border-radius:50%;border:2px dotted var(--teal);display:flex;align-items:center;justify-content:center}
.feature .ring span{width:78px;height:78px;border-radius:50%;background:var(--teal);display:flex;align-items:center;justify-content:center}
.feature p{font-size:24px;line-height:27px;color:var(--navy);font-weight:500}

.section-title{position:absolute;left:0;width:1200px;text-align:center;font-size:52px}
.underline{position:absolute;left:565px;width:70px;height:5px;background:var(--teal)}

/* products */
.product{position:absolute;top:1185px;width:227px;height:466px;border:1.5px solid #6e7790;text-align:center}
.product .shot{margin:3px;height:237px}
.product h3{margin-top:16px;font-size:20px;color:var(--navy);font-weight:600}
.product p{margin:8px auto 0;width:185px;font-size:13px;line-height:21px}
.product .price{margin-top:12px;font-size:19px;font-weight:600;color:var(--navy)}
.product .add{margin:16px auto 0;width:124px;height:33px;border-radius:17px;background:var(--teal-btn);color:var(--navy);font-size:12px;font-weight:600;display:flex;align-items:center;justify-content:center}
.arrow{position:absolute;width:50px;height:50px;border-radius:50%;display:flex;align-items:center;justify-content:center}
.arrow--prev{border:1.5px solid var(--navy);background:var(--white)}
.arrow--next{background:var(--navy)}

/* about */
.about-photo{top:1862px;left:0;width:869px;height:605px}
.about-circle{top:1913px;left:628px;width:506px;height:506px;border-radius:50%;background:var(--navy);color:var(--white);text-align:center}
.about-circle h2{margin-top:80px;color:var(--white);font-size:50px}
.about-circle .bar{margin:12px auto 0;width:70px;height:5px;background:var(--teal)}
.about-circle p{margin:36px auto 0;width:410px;font-size:14px;line-height:27px}

/* testimonials */
.review{position:absolute;top:2759px;width:294px;height:283px;background:var(--teal-soft)}
.review .quote{position:absolute;top:-10px;left:110px;width:73px;height:73px;border-radius:50%;background:var(--navy);display:flex;align-items:center;justify-content:center;color:var(--white);font-family:"Montserrat",sans-serif;font-size:56px;font-weight:700;padding-top:22px}
.review p{position:absolute;top:66px;left:23px;width:248px;font-size:15px;line-height:24px;font-style:italic;text-align:justify}
.review .avatar{position:absolute;top:198px;left:34px;width:72px;height:72px;border-radius:50%;background:radial-gradient(circle at 50% 40%,#a47a5e,#3a2a24)}
.review .name{position:absolute;top:212px;left:122px;font-size:16px;font-weight:600;color:var(--navy)}
.review .stars{position:absolute;top:236px;left:122px;font-size:11px;color:var(--star);letter-spacing:1px}

/* newsletter */
.newsletter{top:3246px;left:0;width:1200px;height:271px;background:var(--teal)}
.newsletter h2{position:absolute;top:62px;left:68px;font-family:"Poppins",sans-serif;font-weight:500;font-size:45px;line-height:52px}
.signup{position:absolute;top:115px;left:506px;width:628px;height:90px;border-radius:8px;background:var(--white);overflow:hidden;display:flex}
.signup span{flex:1;padding-left:26px;display:flex;align-items:center;font-size:16px;color:#707070}
.signup b{width:149px;background:var(--navy);color:var(--white);display:flex;align-items:center;justify-content:center;font-size:18px}

/* footer */
.footer{top:3517px;left:0;width:1200px;height:376px;background:var(--navy);color:var(--white)}
.footer h4{position:absolute;top:110px;font-size:23px;font-weight:500}
.footer .rule{position:absolute;top:137px;left:385px;width:749px;height:1px;background:rgba(255,255,255,.45)}
.footer ul{position:absolute;top:168px;list-style:none;font-size:14px;line-height:26px}
.footer li::before{content:"";display:inline-block;width:9px;height:9px;border-radius:50%;background:var(--teal);margin-right:14px}
.contact{position:absolute;left:883px;display:flex;gap:14px;font-size:13.5px;line-height:18px}
.contact i{width:28px;height:28px;border-radius:4px;background:var(--teal);flex:none;display:flex;align-items:center;justify-content:center}
.bottom{top:3893px;left:0;width:1200px;height:54px;background:var(--navy-dark);color:var(--white);font-size:12px}
.cards{position:absolute;top:20px;left:650px;display:flex;gap:4px}
.cards span{width:25px;height:16px;border-radius:2px;background:#d8dde8}
.social{position:absolute;top:15px;left:1013px;display:flex;gap:6px}
.social span{width:25px;height:25px;border-radius:3px;background:var(--teal)}
</style>
</head>
<body>

<!-- header -->
<div class="brand-mark" style="top:15px;left:69px;width:177px;height:177px;font-size:24px">MAPLE<br>PAWS</div>
<nav class="nav">
  <span class="active">Home</span><span>About Us</span><span>Products ▾</span><span>Contact Us</span>
</nav>
<div class="btn-cart"><svg width="16" height="14" viewBox="0 0 16 14"><path d="M0 1h3l2 8h9l2-6H4" fill="none" stroke="#14245a" stroke-width="1.8"/><circle cx="6" cy="12" r="1.4" fill="#14245a"/><circle cx="13" cy="12" r="1.4" fill="#14245a"/></svg>My Cart</div>
<div class="btn-login"><svg width="12" height="13" viewBox="0 0 12 13"><circle cx="6" cy="3.5" r="3" fill="#fff"/><path d="M0 13c0-4 2.5-6 6-6s6 2 6 6z" fill="#fff"/></svg>Login</div>

<!-- hero -->
<div class="abs hero-bg"></div>
<h1 class="abs hero-title">MAPLE<br>PAWS</h1>
<p class="abs hero-text">Lorem ipsum dolor sit amet, consectetur adipiscing elit. Etiam a turpis ligula. Quisque dolor ante, lacinia ut velit sit amet, posuere bibendum .</p>
<a class="pill pill--navy" style="top:604px;left:69px;width:219px;height:61px;font-size:19px">SHOP NOW <span class="dot"><svg width="8" height="8" viewBox="0 0 8 8"><path d="M2 1l3 3-3 3" stroke="#14245a" stroke-width="1.6" fill="none"/></svg></span></a>
<svg class="abs hero-photo" viewBox="0 0 602 660" role="img" aria-label="Photo of a beagle puppy sitting in front of a teal arch">
  <path d="M0 639V245A255 255 0 0 1 255 -10H300A255 255 0 0 1 557 245V639Z" fill="#9fd7d3" transform="translate(0,37)"/>
  <path d="M342 20A242 242 0 0 1 572 262V620" fill="none" stroke="#14245a" stroke-width="1.5"/>
  <ellipse cx="300" cy="360" rx="190" ry="290" fill="url(#beagle)"/>
  <defs><radialGradient id="beagle" cx="50%" cy="45%" r="60%"><stop offset="0" stop-color="#f2ece4"/><stop offset=".6" stop-color="#c9a47a"/><stop offset="1" stop-color="#6e4a2c" stop-opacity=".9"/></radialGradient></defs>
</svg>

<!-- features -->
<div class="feature" style="left:71px"><div class="ring"><span><svg width="44" height="30" viewBox="0 0 44 30"><rect x="1" y="3" width="28" height="18" rx="2" fill="#14245a"/><path d="M29 9h8l6 7v5H29z" fill="#14245a"/><circle cx="10" cy="24" r="4" fill="#14245a" stroke="#9fd7d3" stroke-width="2"/><circle cx="35" cy="24" r="4" fill="#14245a" stroke="#9fd7d3" stroke-width="2"/></svg></span></div><p>Free<br>Shipping</p></div>
<div class="feature" style="left:345px"><div class="ring"><span><svg width="30" height="38" viewBox="0 0 30 38"><path d="M9 2h12l-3 7h-6z" fill="#14245a"/><path d="M11 10h8c9 6 11 14 9 20-2 6-24 6-26 0-2-6 0-14 9-20z" fill="#14245a"/><text x="15" y="30" text-anchor="middle" font-size="13" font-family="Poppins" font-weight="600" fill="#9fd7d3">$</text></svg></span></div><p>Money<br>Guarantee</p></div>
<div class="feature" style="left:643px"><div class="ring"><span><svg width="36" height="36" viewBox="0 0 36 36"><rect x="3" y="7" width="26" height="26" fill="none" stroke="#14245a" stroke-width="3"/><path d="M9 19l6 6L33 4" fill="none" stroke="#14245a" stroke-width="4"/></svg></span></div><p>Quality<br>Assured</p></div>
<div class="feature" style="left:910px"><div class="ring"><span><svg width="40" height="34" viewBox="0 0 40 34"><rect x="14" y="2" width="24" height="15" rx="2" fill="#14245a" transform="rotate(-15 26 10)"/><path d="M2 20l10-5 12 2-2 4h-8l9 1 9-4-6 8-14 5H2z" fill="#14245a"/></svg></span></div><p>Secure<br>Payment</p></div>

<!-- products -->
<h2 class="section-title heading" style="top:1040px">OUR PRODUCTS</h2>
<div class="underline" style="top:1117px"></div>
<div class="arrow arrow--prev" style="top:1391px;left:52px"><svg width="12" height="14" viewBox="0 0 12 14"><path d="M9 1L3 7l6 6" stroke="#14245a" stroke-width="2.6" fill="none"/></svg></div>
<div class="arrow arrow--next" style="top:1391px;left:1104px"><svg width="12" height="14" viewBox="0 0 12 14"><path d="M3 1l6 6-6 6" stroke="#fff" stroke-width="2.6" fill="none"/></svg></div>

<div class="product" style="left:127px">
  <div class="shot" role="img" aria-label="Product photo: white bulldog puppy with food bowl" style="background:linear-gradient(#f3f3f3 60%,#d9c9bb 78%,#c8532c 92%)"></div>
  <h3>Product 1</h3><p>Lorem ipsum dolor sit amet, consectetur adipis elit. Etiam a turpis ligula.</p>
  <div class="price">$25.99</div><div class="add">ADD TO CART</div>
</div>
<div class="product" style="left:369px">
  <div class="shot" role="img" aria-label="Product photo: white terrier with grooming bottles" style="background:radial-gradient(circle at 45% 50%,#f2f4f4 0 30%,#4fbfdf 60%)"></div>
  <h3>Product 2</h3><p>Lorem ipsum dolor sit amet, consectetur adipis elit. Etiam a turpis ligula.</p>
  <div class="price">$25.99</div><div class="add">ADD TO CART</div>
</div>
<div class="product" style="left:610px">
  <div class="shot" role="img" aria-label="Product photo: comb, teal harness and pink bag holder" style="background:linear-gradient(160deg,#f1f1f1 30%,#b5e3e2 55%,#f1f1f1 75%,#f3c4d4)"></div>
  <h3>Product 3</h3><p>Lorem ipsum dolor sit amet, consectetur adipis elit. Etiam a turpis ligula.</p>
  <div class="price">$25.99</div><div class="add">ADD TO CART</div>
</div>
<div class="product" style="left:852px">
  <div class="shot" role="img" aria-label="Product photo: terrier wearing a red bow tie collar" style="background:radial-gradient(circle at 50% 55%,#f6f2ec 0 25%,#a67550 45%,#f2c7ad 70%)"></div>
  <h3>Product 4</h3><p>Lorem ipsum dolor sit amet, consectetur adipis elit. Etiam a turpis ligula.</p>
  <div class="price">$25.99</div><div class="add">ADD TO CART</div>
</div>

<a class="pill pill--navy" style="top:1720px;left:449px;width:300px;height:61px;font-size:19px">VIEW ALL PRODUCTS <span class="dot"><svg width="8" height="8" viewBox="0 0 8 8"><path d="M2 1l3 3-3 3" stroke="#14245a" stroke-width="1.6" fill="none"/></svg></span></a>

<!-- about -->
<div class="abs about-photo" role="img" aria-label="Close-up photo of a happy long-haired brown and white dog" style="background:radial-gradient(ellipse at 35% 50%,#e9dcc6 0 18%,#a9652f 38%,#4c5a2a 70%,#2f3d1e)"></div>
<svg class="abs" style="top:1862px;left:560px" width="310" height="605" viewBox="0 0 310 605"><path d="M310 0H255A330 330 0 0 0 40 330A330 330 0 0 0 255 605H310Z" fill="#6f7567" opacity=".55"/></svg>
<div class="abs about-circle">
  <h2>ABOUT US</h2><div class="bar"></div>
  <p>Lorem ipsum dolor sit amet, consectetur adipiscing elit, sed do eiusmod tempor incididunt ut labore et dolore magna aliqua. Ut enim ad minim veniam, quis nostrud exercitation ullamco laboris nisi ut aliquip ex ea commo do consequat. Duis aute irure dolor in reprehenderit in voluptate velit esse cillum dolore eu fugiat.</p>
</div>
<a class="pill" style="top:2294px;left:781px;width:201px;height:58px;font-size:19px;background:var(--teal-btn);color:var(--navy)">READ MORE <span class="dot" style="background:var(--navy)"><svg width="8" height="8" viewBox="0 0 8 8"><path d="M2 1l3 3-3 3" stroke="#fff" stroke-width="1.6" fill="none"/></svg></span></a>

<!-- testimonials -->
<h2 class="section-title heading" style="top:2567px">OUR TESTIMONIALS</h2>
<div class="underline" style="top:2644px"></div>
<div class="arrow arrow--prev" style="top:2857px;left:52px"><svg width="12" height="14" viewBox="0 0 12 14"><path d="M9 1L3 7l6 6" stroke="#14245a" stroke-width="2.6" fill="none"/></svg></div>
<div class="arrow arrow--next" style="top:2857px;left:1104px"><svg width="12" height="14" viewBox="0 0 12 14"><path d="M3 1l6 6-6 6" stroke="#fff" stroke-width="2.6" fill="none"/></svg></div>

<div class="review" style="left:141px"><div class="quote">“</div>
  <p>Lorem ipsum dolor sit amet, con sectetur adipiscing elit. Aliquam molestie ut dui in placerat. Nam malesuada eros arcu, a porttitor nulla sodales dictum.</p>
  <div class="avatar" role="img" aria-label="Customer portrait"></div><div class="name">Clara Bennet</div><div class="stars">★★★★★</div></div>
<div class="review" style="left:460px"><div class="quote">“</div>
  <p>Lorem ipsum dolor sit amet, con sectetur adipiscing elit. Aliquam molestie ut dui in placerat. Nam malesuada eros arcu, a porttitor nulla sodales dictum.</p>
  <div class="avatar" role="img" aria-label="Customer portrait"></div><div class="name">Marcus Hale</div><div class="stars">★★★★★</div></div>
<div class="review" style="left:779px"><div class="quote">“</div>
  <p>Lorem ipsum dolor sit amet, con sectetur adipiscing elit. Aliquam molestie ut dui in placerat. Nam malesuada eros arcu, a porttitor nulla sodales dictum.</p>
  <div class="avatar" role="img" aria-label="Customer portrait"></div><div class="name">Ivy Morrow</div><div class="stars">★★★★★</div></div>

<a class="pill pill--navy" style="top:3103px;left:449px;width:300px;height:61px;font-size:19px">VIEW ALL REVIEWS <span class="dot"><svg width="8" height="8" viewBox="0 0 8 8"><path d="M2 1l3 3-3 3" stroke="#14245a" stroke-width="1.6" fill="none"/></svg></span></a>

<!-- newsletter -->
<section class="abs newsletter">
  <h2>Sign up for our<br>newsletter and<br>get 10% discount!</h2>
  <div class="signup"><span>Enter Email Address</span><b>SIGNUP</b></div>
</section>

<!-- footer -->
<footer class="abs footer">
  <div class="brand-mark" style="top:109px;left:101px;width:222px;height:222px;font-size:30px">MAPLE<br>PAWS</div>
  <h4 style="left:385px">Quick Links</h4>
  <h4 style="left:616px">Help &amp; Support</h4>
  <h4 style="left:883px">Contact Us</h4>
  <div class="rule"></div>
  <ul style="left:385px"><li>About Us</li><li>Products</li><li>Contact Us</li></ul>
  <ul style="left:616px"><li>Refund policy</li><li>Privacy policy</li><li>Terms of service</li><li>Shipping policy</li><li>Contact information</li></ul>
  <div class="contact" style="top:169px"><i><svg width="14" height="14" viewBox="0 0 14 14"><path d="M3 1l3 3-2 2c1 2 2 3 4 4l2-2 3 3-2 2C6 13 1 8 1 3z" fill="#14245a"/></svg></i><div>CALL US<br>0155 210 4478</div></div>
  <div class="contact" style="top:218px"><i><svg width="14" height="11" viewBox="0 0 14 11"><rect width="14" height="11" rx="1" fill="#14245a"/><path d="M1 1l6 5 6-5" stroke="#9fd7d3" fill="none"/></svg></i><div>EMAIL US<br>hello@maplepaws.shop</div></div>
  <div class="contact" style="top:270px"><i><svg width="12" height="16" viewBox="0 0 12 16"><path d="M6 0a6 6 0 0 1 6 6c0 4-6 10-6 10S0 10 0 6a6 6 0 0 1 6-6z" fill="#14245a"/><circle cx="6" cy="6" r="2" fill="#9fd7d3"/></svg></i><div>Address line dummy here<br>Addres line dummy</div></div>
</footer>
<div class="abs bottom">
  <span class="abs" style="top:19px;left:69px">Copyright © 2025 All Rights Reserved By Company Name</span>
  <div class="cards"><span></span><span></span><span></span><span></span><span></span></div>
  <div class="social"><span></span><span></span><span></span><span></span></div>
</div>

</body>
</html>
```